Bright Harbour Charity - helping the disadvantaged

I would like a new web site design for my charity BRIGHT HARBOUR. The charity provides help for the disadvantaged. See current site
brightharbour.org.au for details. Please refer to the current site for information on the charity. The objectives of the charity are in the "about us" tab. You will also notice on the site that we provide information about events that we sponsor an area for this should be provided on the site.

Target Market(s)

We have two targets:
1. Individuals and Businesses that will donate money to the charity.
2. Individuals that are in need of support from the charity.

Industry/Entity Type

Charity

Requirements
Must have
• Ability for individuals to be able to understand the type of support we can provide.
Nice to have
• Our logo should be prominate on each pages
Should not have
• Should be use modern fonts

```html
<!DOCTYPE html>
<html lang="en">
<head>
<meta charset="utf-8">
<title>Bright Harbour – Helping the Disadvantaged</title>
<link href="https://fonts.googleapis.com/css2?family=Arimo:ital,wght@0,400;0,700;1,400&display=swap" rel="stylesheet">
<style>
:root{
  --page:#cdc9c0;
  --panel:#f6f1e4;
  --panel-edge:#e2dccb;
  --frame:#c8c2ac;
  --gold-1:#e9c867;
  --gold-2:#c99a2a;
  --nav-text:#a36b1c;
  --heading-green:#1f3f1c;
  --logo-green:#3f8a2a;
  --body-grey:#77736c;
  --dark:#3a3630;
  --orange:#e8914a;
  --orange-deep:#ec8a33;
  --button-grey:#dcd7cc;
  --accent-red:#c4161c;
  --white:#ffffff;
}
*{box-sizing:border-box;margin:0;padding:0}
html,body{width:936px;height:1200px;overflow:hidden}
body{background:var(--page);font-family:"Arimo",Arial,sans-serif;position:relative;color:var(--dark)}
.abs{position:absolute}

.nav-panel{left:44px;top:20px;width:612px;height:50px;background:var(--panel);border-radius:5px 0 0 0;border:1px solid var(--panel-edge)}
.nav{left:75px;top:38px;font-size:12px;color:var(--nav-text);display:flex;gap:0;white-space:nowrap}
.nav span.sep{margin:0 8px;color:#b48a4a}
.search-panel{left:656px;top:20px;width:233px;height:50px;background:var(--panel);border-radius:0 5px 0 0;border:1px solid var(--panel-edge)}
.search{left:683px;top:30px;width:180px;height:27px;border-radius:7px;background:#fbf9f3;border:1px solid #d8d2c2;box-shadow:inset 0 1px 2px rgba(0,0,0,.15)}
.search span{position:absolute;right:6px;top:6px;font-size:12px;color:#555;border-left:1px solid #999;padding-left:3px;line-height:13px}

.banner-frame{left:44px;top:70px;width:845px;height:222px;background:var(--frame)}
.banner{left:51px;top:80px;width:828px;height:202px;background:linear-gradient(90deg,var(--gold-1),#e2b64a 50%,var(--gold-2))}
.banner-photo{left:555px;top:80px;width:324px;height:202px;background:linear-gradient(90deg,rgba(233,200,103,0),#b58650 35%,#8f6a3f)}
.logo{left:82px;top:168px;display:flex;align-items:center;gap:10px}
.logo .dot{width:16px;height:16px;border-radius:50%;background:var(--orange)}
.logo .name{font-size:38px;color:var(--logo-green);letter-spacing:1px;line-height:1}

.main{left:44px;top:310px;width:612px;height:858px;background:var(--panel);border:1px solid var(--panel-edge);border-radius:4px 0 0 4px}
.side{left:656px;top:310px;width:233px;height:858px;background:var(--panel);border:1px solid var(--panel-edge);border-radius:0 4px 4px 0}

.announce-label{left:68px;top:327px;font-size:11.5px;color:#222}
.announce-link{left:69px;top:347px;font-size:12px;color:var(--orange)}
.btn{background:var(--button-grey);color:#6c6860;font-style:italic;font-size:12px;display:flex;align-items:center;justify-content:center}
.view-btn{left:342px;top:339px;width:86px;height:23px}
.divider{left:115px;top:369px;width:465px;border-top:1px dashed #d3ccba}

.photo-main{left:106px;top:383px;width:448px;height:275px;background:linear-gradient(135deg,#6f8d4a,#b9875c 45%,#3d8aa0);box-shadow:0 3px 6px rgba(0,0,0,.3)}
.story{left:70px;width:540px;font-size:12.5px;line-height:17.3px;color:var(--body-grey)}
.story-1{top:676px}
.story-2{top:938px}
.read-1{left:71px;top:754px;width:86px;height:23px}
.read-2{left:71px;top:1017px;width:86px;height:23px}
.event-banner{left:69px;top:802px;width:533px;height:111px;background:#050505;box-shadow:0 3px 6px rgba(0,0,0,.35)}
.event-badge{left:86px;top:810px;width:40px;height:14px;background:#e8e8e8}
.event-strip{left:69px;top:868px;width:533px;height:28px;background:linear-gradient(90deg,#f0a24a,#b5a6d8,#4fb8b0,#e6c33c,#f08aa0,#9aa0e0)}

.side-title{left:670px;top:323px;font-size:13px;font-weight:700;color:var(--heading-green);line-height:13.5px}
.bullets{left:671px;top:397px;list-style:none;font-size:11.5px;color:#444;line-height:23px}
.bullets li::before{content:"";display:inline-block;width:6px;height:6px;border-radius:50%;background:#555;margin-right:6px;vertical-align:1px}
.bullets li.cont::before{visibility:hidden}
.side-head{left:668px;font-size:13px;font-weight:700;color:var(--heading-green);display:flex;align-items:center;gap:7px}
.side-head::before{content:"";width:11px;height:11px;border-radius:50%;background:var(--accent-red)}
.head-art{top:575px}
.head-harmony{top:796px}
.art-img{left:665px;top:605px;width:188px;height:126px;background:radial-gradient(circle,#e9b93b,#b0321e 55%,#5a1c1a);box-shadow:0 2px 5px rgba(0,0,0,.3)}
.harmony-img{left:665px;top:823px;width:188px;height:65px;background:linear-gradient(90deg,#d8a56a,#e6c33c,#ef8fb0,#e8823a,#4fb8b0)}
.belongs{left:698px;top:898px;width:124px;text-align:center;font-size:13px;font-weight:700;color:#111;padding-bottom:4px;border-bottom:1px solid var(--accent-red)}
.read-art{left:669px;top:760px;width:85px;height:23px}
.read-harmony{left:669px;top:940px;width:85px;height:23px}

.donate-box{left:677px;top:976px;width:206px;height:181px;border-radius:8px;background:linear-gradient(180deg,#f7c89a,var(--orange-deep));box-shadow:0 2px 4px rgba(0,0,0,.2)}
.arrow{width:12px;height:12px}
.donate-head{left:686px;top:990px;display:flex;align-items:center;gap:10px;font-size:15px;color:var(--white);text-decoration:underline}
.donate-text{left:691px;top:1011px;width:180px;font-size:12px;line-height:15px;color:#222}
.click-btn{left:692px;top:1075px;width:165px;height:26px;background:#241109;border:1px solid #fff;border-radius:8px;color:var(--white);font-size:17px;display:flex;align-items:center;justify-content:center}
.apply{left:686px;top:1117px;display:flex;align-items:center;gap:10px;font-size:16px;color:#2a1608}

.copyright{left:538px;top:1180px;font-size:10.5px;font-weight:700;color:var(--white)}
</style>
</head>
<body>
<div class="abs nav-panel"></div>
<nav class="abs nav">
  <span>Home</span><span class="sep">|</span><span>About Us</span><span class="sep">|</span><span>Donate</span><span class="sep">|</span><span>Apply</span><span class="sep">|</span><span>Pledge</span><span class="sep">|</span><span>Nominate</span><span class="sep">|</span><span>Events</span><span class="sep">|</span><span>Contact Us</span><span class="sep">|</span><span>Directors</span>
</nav>
<div class="abs search-panel"></div>
<div class="abs search"><span>Search</span></div>

<div class="abs banner-frame"></div>
<div class="abs banner"></div>
<div class="abs banner-photo" role="img" aria-label="Photo of a smiling child in a wicker basket wearing angel wings"></div>
<div class="abs logo"><span class="dot"></span><span class="name">BRIGHT HARBOUR</span></div>

<main class="abs main"></main>
<aside class="abs side"></aside>

<p class="abs announce-label">ANNOUNCEMENT:</p>
<p class="abs announce-link">Harmony Day Information sheet &amp; Booking form</p>
<div class="abs btn view-btn">Click to view</div>
<div class="abs divider"></div>

<div class="abs photo-main" role="img" aria-label="Photo of a smiling red-haired girl on a playground swing"></div>
<p class="abs story story-1">Harmony Day Event 2012 Harmony Celebration Day - "EVERYONE BELONGS" Date:Satyurday 24th March 2012&nbsp; Venue: Hillcrest Care Education Facilities, Westbury Road, Linfield. Time: 10am - 3 pm Harmony.Bright Harbour &amp; Hillcrest Care will be holding a multicultural market and art exhibition combined with a community harmony day being held on site at....</p>
<div class="abs btn read-1">Read more</div>

<div class="abs event-banner" role="img" aria-label="Harmony Day 24 March banner with a row of figures holding hands"></div>
<div class="abs event-badge"></div>
<div class="abs event-strip"></div>

<p class="abs story story-2">Harmony Day Event 2012 Harmony Celebration Day - "EVERYONE BELONGS" Date:Satyurday 24th March 2012&nbsp; Venue: Hillcrest Care Education Facilities, Westbury Road, Linfield. Time: 10am - 3 pm Harmony.Bright Harbour &amp; Hillcrest Care will be holding a multicultural market and art exhibition combined with a community harmony day being held on site at....</p>
<div class="abs btn read-2">Read more</div>

<h2 class="abs side-title">Saturday 24th March<br>at Hillcrest Care Education<br>Facilities Westbury &amp; Jubilee<br>Roads Linfield</h2>
<ul class="abs bullets">
  <li>Lots of prizes to be Won!</li>
  <li>Free Entry &amp; variety of free activities</li>
  <li>Art Exhibition</li>
  <li>Perfomance</li>
  <li>Community service Info stalls</li>
  <li>Multicultural food market stalls</li>
  <li class="cont">Multural arts &amp; craft market stalls.</li>
</ul>

<h3 class="abs side-head head-art">Art Exhibition</h3>
<div class="abs art-img" role="img" aria-label="Dot painting artwork in red, yellow and white"></div>
<div class="abs btn read-art">Read more</div>

<h3 class="abs side-head head-harmony">Harmony Day</h3>
<div class="abs harmony-img" role="img" aria-label="Colourful figures holding hands"></div>
<p class="abs belongs">everyone Belongs</p>
<div class="abs btn read-harmony">Read more</div>

<div class="abs donate-box"></div>
<div class="abs donate-head"><svg class="arrow" viewBox="0 0 12 12"><path d="M1 1l5 5-5 5M6 1l5 5-5 5" fill="none" stroke="#fff" stroke-width="2"/></svg><span>Donate</span></div>
<p class="abs donate-text">If you wish to make a donation to Bright Harbour please fill out and submit the form below or contact us directly.</p>
<div class="abs click-btn">Click here</div>
<div class="abs apply"><svg class="arrow" viewBox="0 0 12 12"><path d="M1 1l5 5-5 5M6 1l5 5-5 5" fill="none" stroke="#fff" stroke-width="2"/></svg><span>Apply</span></div>

<p class="abs copyright">Copyright © 2012 Bright Harbour Proprietary Limited. All Rights Reserved.</p>
</body>
</html>
```